Business card with logo for a family psychologist

I need a business card for my private practice in the urban Chicago area as a psychologist. I see families and individuals who are going through difficult times - divorce, separation, illness, or trauma. I want to project hopefulness, competence, and caring.

Target Market(s)

Adults, other professionals - such as physicans and lawyers

Industry/Entity Type

Health Care

Contact Information for Business Card

Front should have my name and credentials; back should have location information including my email, phone

Font styles to use
Serif
Decorative
Script

Requirements
Must have
• Unique logo
Should not have
• No pictures or icons of people; no black

```html
<!DOCTYPE html>
<html lang="en">
<head>
<meta charset="utf-8">
<title>Whitfield Psychology – Business Card</title>
<link href="https://fonts.googleapis.com/css2?family=Tinos:wght@400;700&display=swap" rel="stylesheet">
<style>
  :root {
    --page-bg: #ece8e4;
    --purple: #b534b9;
    --purple-deep: #9420a0;
    --purple-light: #c548c8;
    --card-white: #f7f7f7;
    --card-grey: #e6e6e6;
    --text-grey: #8e8e8e;
    --rule-grey: #d2d2d2;
    --white: #ffffff;
  }
  * { margin: 0; padding: 0; box-sizing: border-box; }
  html, body {
    width: 1200px; height: 780px; overflow: hidden;
    background: var(--page-bg);
    font-family: "Tinos", "Times New Roman", serif;
  }
  .canvas { position: relative; width: 1200px; height: 780px; }

  .card {
    position: absolute;
    border-radius: 18px;
    overflow: hidden;
    box-shadow: 0 10px 28px rgba(60, 30, 60, 0.22);
  }

  /* Front */
  .card-front {
    left: 70px; top: 225px; width: 580px; height: 330px;
    background: radial-gradient(ellipse at 70% 25%, var(--purple-light), var(--purple) 45%, var(--purple-deep));
    color: var(--white);
  }
  .front-seal {
    position: absolute; left: 215px; top: 20px;
    width: 290px; height: 290px; border-radius: 50%;
    border: 2px solid rgba(255,255,255,0.07);
    background: rgba(255,255,255,0.04);
  }
  .front-intro {
    position: absolute; left: 70px; top: 48px;
    font-size: 24px; line-height: 24px;
  }
  .front-topics {
    position: absolute; left: 70px; top: 104px;
    font-size: 50px; line-height: 44px; letter-spacing: -0.5px;
  }
  .front-name {
    position: absolute; left: 40px; bottom: 40px;
    font-size: 29px; font-weight: 700; letter-spacing: 1px;
    text-shadow: 0 2px 3px rgba(0,0,0,0.25);
  }

  /* Back */
  .card-back {
    left: 745px; top: 110px; width: 330px; height: 560px;
    background: linear-gradient(160deg, var(--card-white), var(--card-grey));
    text-align: center;
  }
  .back-brand {
    position: absolute; left: 0; right: 0; top: 70px;
    display: flex; flex-direction: column; align-items: center; gap: 18px;
  }
  .brand-circle {
    width: 120px; height: 120px; border-radius: 50%;
    border: 3px solid var(--purple);
  }
  .brand-name {
    font-size: 22px; color: var(--purple); letter-spacing: 1.5px;
  }
  .back-address {
    position: absolute; left: 0; right: 0; top: 296px;
    font-size: 19px; line-height: 21px; color: var(--text-grey);
  }
  .contact-label {
    display: block; font-size: 15px; color: var(--purple); font-weight: 700;
  }
  .contact-value {
    display: block; font-size: 19px; color: var(--text-grey); letter-spacing: 0.5px;
  }
  .back-phone { position: absolute; left: 0; right: 0; top: 384px; }
  .back-rule {
    position: absolute; left: 30px; right: 30px; top: 437px;
    height: 1px; background: var(--rule-grey);
  }
  .back-email { position: absolute; left: 0; right: 0; top: 446px; }
  .back-email .contact-value { font-size: 17px; }
  .back-band {
    position: absolute; left: 0; right: 0; bottom: 0; height: 42px;
    background: linear-gradient(90deg, var(--purple-deep), var(--purple));
    border-top: 3px solid #ffffff;
    box-shadow: 0 -2px 0 var(--rule-grey);
  }
</style>
</head>
<body>
<main class="canvas">
  <section class="card card-front" aria-label="Card front">
    <div class="front-seal" aria-hidden="true"></div>
    <p class="front-intro">families and individuals who are<br>going through difficult times</p>
    <p class="front-topics">divorce | separation<br>illness or trauma</p>
    <p class="front-name">Dana Whitfield, Ph.D.</p>
  </section>

  <section class="card card-back" aria-label="Card back">
    <div class="back-brand">
      <div class="brand-circle" aria-hidden="true"></div>
      <p class="brand-name">Whitfield Psychology</p>
    </div>
    <address class="back-address" style="font-style: normal;">
      240 N. Lakeview Suite 810<br>Chicago<br>Illinois 60601
    </address>
    <div class="back-phone">
      <span class="contact-label">Phone</span>
      <span class="contact-value">312-555-0148</span>
    </div>
    <div class="back-rule"></div>
    <div class="back-email">
      <span class="contact-label">Email</span>
      <span class="contact-value">drdanawhitfield@example.com</span>
    </div>
    <div class="back-band"></div>
  </section>
</main>
</body>
</html>
```